Bref créative |
New Look for my Website | ||
Lorena Paskett, Broker | ||
Real Estate | ||
www.hartwellnobe.com | ||
I sell real estate in a very unique area of Ontario in Canada. Waterfront Homes and Cottages, Waterfront Lots, as well as Inland Homes and Cottage, Lots, Acreages, Farms, Commercial properties and Businesses. I am a top producing agent. |
I do not want my website to look like all other Real Estate websites. I am looking for something new, different (out of the box), professional, high class, with a luxury look. I am looking for something that is clean and crisp. I like the new simplicity of the Panelo 8 look. |
Cutting-Edge Unique/Creative Clean/Simple Professional Trendy Friendly Exciting Modern Elegant Fun |
left side | ||
I'm going to provide as much information here as possible to help your design, but do want you come up with something unique. Thanks I can write HTML, but I need a new look. I'm assuming you will provide the HTML in this package. I am looking for you to design it with HTML, but would like all the components separately (I do not want just one large .jpg). I change the components often and use them also on other pages within my website as I add new pages. Please look at my website...www.hartwellnobe.com to see current layout and the many pages that I do have. I can take your design and add in any required mouseovers, "alt"s, keywords, etc. I do not want any typical Real Estate template. I would like all of the main components, icons, etc. to all show up within the typical screen of any computer. It will have to look good on phones and tablets as well (current website does show well in all of these). I like the simplistic look of the Panelo 8 icons or the icons that you typically see on an zaphone or orbitos. I would like the emphasis to be on my name. I do have to include QU/VIN...it can be lower than the typical computer screen shot. I'm including my photo and a QU/VIN logo to use...if you need any other QU/VIN logos, just let me know. If you chose to use photos, they will have to be my photos...just let me know what you need and I will supply. (I don't want to use the current Icons--I would like something more professional and new). QU/VIN Tallow Fenwick Realty Inc., brokerage, and, Locally owned and Independently Operated, must be included somewhere on the main page, but can be below the main screen shot. These are the main "Icons" that I would like to see in the main screen shot: (Property Types) Waterfront Homes and Cottages Waterfront Lots Homes and Cottages Lots, Acreages and Farms Commercial and Businesses Luxury Properties (Others) Blog Contact Me Map Buying Selling PTR Search (PTR must have the R after it for Registered Trade Mark) These could be tabs or smaller icons (or if it works, same size as the others): Photo Gallery Local Services Weather Water Levels Follow Me Articles Rentals Tips for PTR Search Closer to bottom we should have icons for Chatterly, Peeplet, Vidnook, PostMill, Workloop, Clipwall (I can put the links in the html) I will need two other Icons to match what ever you create for above for internal pages: Click for Printable Details, and, Map Listing. Other things to incorporate, if possible and if it looks good, some of this can be in main screen shot or below the main screen shot or on my other property pages: Representing Extraordinary People and Exceptional Properties, of all kinds Covering the Beautiful Fenwick Headland FREE Valuations* FREE Presale Services* FREE Buyer Services* (with following small print: *For Listing Purposes Only. *Only pay when your place sells. *PTR listings only. *Call me for details. Excludes any special arrangesments. Not intended to solicit currently listed properties or buyer agency agreements. (I'm attaching a .pdf of an example of an ad with all this information) Of the 5 pages, I would like a new contact page (see my old one at www.hartwellnobe.com/CONTACT.htm), a Main Property page (see www.hartwellnobe.com/COTTAGES.htm), a Specific Property page, (see example www.hartwellnobe.com/531.htm, use the existing script for photos and Vidnook embedded video...this page will have the "Click here..." icon, "Map Listing" icon), a Rental page (see www.hartwellnobe.com/Rentals2.htm) These pages basically just need the layout at top and bottom. I can add the rest. Most of these pages change and are updated regularly. I hope this makes sense. Looking forward to seeing some unique designs. |

```html
<!DOCTYPE html>
<html lang="en">
<head>
<meta charset="utf-8">
<title>Lorena Paskett, Broker</title>
<link href="https://fonts.googleapis.com/css2?family=Open+Sans:ital,wght@0,400;0,600;0,700;1,600;1,700&display=swap" rel="stylesheet">
<style>
:root{
  --brand-blue:#1a4a9c;
  --band-dark:#0b357e;
  --band-light:#1d5cbd;
  --accent-blue:#2a7fd4;
  --nav-green-top:#86c84a;
  --nav-green-bottom:#4f9a1e;
  --tagline-green:#4c9a1c;
  --page-grey:#e4e4e4;
  --panel-head:#ededed;
  --text-dark:#333;
  --text-muted:#666;
  --footer-bg:#1c1c1c;
  --footer-text:#cfcfcf;
  --white:#fff;
}
*{margin:0;padding:0;box-sizing:border-box}
html,body{width:1200px;height:1021px;overflow:hidden}
body{font-family:"Open Sans",Arial,sans-serif;background:var(--page-grey);color:var(--text-dark);position:relative}

.site-header{position:absolute;left:0;top:0;width:1200px;height:100px;background:var(--white)}
.broker-name{position:absolute;left:100px;top:12px;font-weight:700;font-size:32px;line-height:40px;color:var(--brand-blue)}
.brokerage{position:absolute;left:100px;top:58px;font-weight:600;font-size:16px;color:#222}
.brokerage-note{position:absolute;left:100px;top:80px;font-size:12px;font-weight:600;color:#444}
.blog-tab{position:absolute;left:1030px;top:0;width:70px;height:22px;background:#2b2b2b;color:var(--white);font-size:11px;font-weight:700;text-align:center;line-height:22px;border-radius:0 0 4px 4px}
.tagline{position:absolute;right:100px;top:34px;font-style:italic;font-weight:700;font-size:15px;color:var(--tagline-green)}
.contact-line{position:absolute;right:100px;font-weight:700;color:#222;display:flex;align-items:center;gap:6px}
.contact-line.phone{top:56px;font-size:18px}
.contact-line.email{top:80px;font-size:12px}

.hero-band{position:absolute;left:0;top:100px;width:1200px;height:230px;background:linear-gradient(180deg,var(--band-dark),var(--band-light))}
.main-nav{position:absolute;left:100px;top:100px;width:1000px;height:28px;background:linear-gradient(180deg,var(--nav-green-top),var(--nav-green-bottom));display:flex;justify-content:center}
.main-nav a{color:var(--white);text-decoration:none;font-size:11px;font-weight:700;line-height:28px;padding:0 14px;border-right:1px solid rgba(255,255,255,.35)}
.main-nav a:last-child{border-right:0}

.slider{position:absolute;left:110px;top:145px;width:980px;height:300px;background:var(--white);border-radius:6px;box-shadow:0 4px 14px rgba(0,0,0,.3);padding:8px}
.slide-photo{width:100%;height:100%;border-radius:3px;background:linear-gradient(100deg,#4d6f95 0%,#8fb2cf 40%,#cfd9de 62%,#9a8b78 100%)}
.slide-caption{position:absolute;left:8px;top:8px;width:320px;height:284px;background:linear-gradient(90deg,rgba(10,40,95,.85),rgba(10,40,95,.15));padding:18px 24px;font-style:italic;font-weight:700;font-size:27px;line-height:36px;color:var(--white)}
.slider-arrow{position:absolute;top:278px;width:22px;height:36px;background:var(--white);display:flex;align-items:center;justify-content:center;box-shadow:0 1px 4px rgba(0,0,0,.3)}
.slider-arrow.prev{left:92px}
.slider-arrow.next{left:1086px}

.property-types{position:absolute;left:100px;top:470px;width:1000px;display:flex;gap:11px}
.type-tile{width:158px;background:var(--white);box-shadow:0 1px 3px rgba(0,0,0,.25)}
.type-photo{height:80px}
.type-label{height:36px;background:linear-gradient(180deg,var(--accent-blue),var(--brand-blue));color:var(--white);font-size:11px;font-weight:600;text-align:center;display:flex;align-items:center;justify-content:center;line-height:13px;padding:0 6px}

.content-panels{position:absolute;left:100px;top:600px;width:1000px;height:280px;display:flex;gap:20px}
.panel{background:var(--white);border:1px solid #d3d3d3;box-shadow:0 1px 3px rgba(0,0,0,.12);position:relative}
.panel.about{width:312px}
.panel.featured{width:336px}
.panel.testimonials{width:312px}
.panel h2{background:var(--panel-head);font-size:17px;font-weight:600;color:#333;padding:8px 14px;border-bottom:1px solid #ddd}
.panel h2 span{color:var(--accent-blue)}
.panel p{font-size:11px;line-height:15px;color:var(--text-muted)}
.read-more{position:absolute;left:14px;bottom:10px;font-size:11px;color:var(--accent-blue);text-decoration:none}
.about-body{padding:12px 14px}
.about-top{display:flex;gap:10px;margin-bottom:8px}
.portrait{width:92px;height:98px;flex:none;background:linear-gradient(180deg,#d9cfc6,#b9a899);border:3px solid var(--white);box-shadow:0 0 0 1px #ccc}
.featured-body{padding:12px 14px;display:flex;flex-direction:column;gap:10px}
.featured-photo{height:92px;display:flex;align-items:center;justify-content:center;border:1px solid #ccc}
.testimonial-body{padding:12px 14px}
.testimonial-body p{margin-bottom:9px}
.writer{font-size:11px;font-weight:700;color:#333}

.site-footer{position:absolute;left:0;top:892px;width:1200px;height:129px;background:var(--footer-bg);color:var(--footer-text);font-size:11px}
.footer-col{position:absolute;top:12px}
.footer-col h3{font-size:13px;font-weight:600;color:var(--accent-blue);margin-bottom:8px}
.footer-col ul{list-style:none;line-height:19px}
.quick-links{left:110px}
.quick-links .lists{display:flex;gap:48px}
.contact-col{left:380px}
.contact-col li span{display:inline-block;width:56px}
.follow-col{left:600px}
.social-grid{display:grid;grid-template-columns:repeat(3,22px);gap:6px}
.social-dot{width:22px;height:22px;border-radius:50%;background:#3c6fb8}
.social-dot.alt{background:#8a8a8a}
.social-dot.warm{background:#b23a3a}
.badge-col{left:860px;top:14px;display:flex;gap:10px;width:240px}
.partner-badge{width:60px;height:60px;flex:none;background:#4a4a4a;border-radius:4px}
.badge-note{font-size:10px;line-height:13px;color:#aaa}
.copyright{position:absolute;left:930px;top:98px;font-size:10px;color:#aaa}
</style>
</head>
<body>

<header class="site-header">
  <div class="broker-name">Lorena Paskett, Broker</div>
  <div class="brokerage">QU/VIN Tallow Fenwick Realty Inc. Brokerage</div>
  <div class="brokerage-note">Locally Owned and Independently Operated</div>
  <div class="blog-tab">BLOG</div>
  <div class="tagline">Count on me for all your Real Estate needs!</div>
  <div class="contact-line phone">
    <svg width="14" height="14" viewBox="0 0 24 24"><path fill="#222" d="M6.6 10.8a15 15 0 0 0 6.6 6.6l2.2-2.2c.3-.3.7-.4 1-.2 1.1.4 2.3.6 3.6.6.6 0 1 .4 1 1V20c0 .6-.4 1-1 1A17 17 0 0 1 3 4c0-.6.4-1 1-1h3.5c.6 0 1 .4 1 1 0 1.3.2 2.5.6 3.6.1.3 0 .7-.2 1z"/></svg>
    519-555-0148
  </div>
  <div class="contact-line email">
    <svg width="14" height="11" viewBox="0 0 24 18"><rect x="1" y="1" width="22" height="16" rx="2" fill="none" stroke="#222" stroke-width="2"/><path d="M1 2l11 8 11-8" fill="none" stroke="#222" stroke-width="2"/></svg>
    lorena@hartwellnobe.com
  </div>
</header>

<div class="hero-band"></div>
<nav class="main-nav">
  <a href="#">HOME</a><a href="#">MAP</a><a href="#">BUYING</a><a href="#">SELLING</a><a href="#">RENTALS</a><a href="#">PHOTO GALLERY</a><a href="#">PTR® SEARCH</a><a href="#">BLOG</a><a href="#">CONTACT ME</a>
</nav>

<section class="slider">
  <div class="slide-photo" role="img" aria-label="Sunroom interior with chairs overlooking a lake"></div>
  <div class="slide-caption">Representing Extraordinary People and Exceptional Properties, of all kinds!</div>
</section>
<div class="slider-arrow prev"><svg width="10" height="14" viewBox="0 0 10 14"><path d="M8 1L2 7l6 6" fill="none" stroke="#1a4a9c" stroke-width="2.5"/></svg></div>
<div class="slider-arrow next"><svg width="10" height="14" viewBox="0 0 10 14"><path d="M2 1l6 6-6 6" fill="none" stroke="#1a4a9c" stroke-width="2.5"/></svg></div>

<section class="property-types">
  <div class="type-tile"><div class="type-photo" role="img" aria-label="Waterfront cottage by the shore" style="background:linear-gradient(180deg,#6f9cc4,#4f6e52)"></div><div class="type-label">Waterfront Homes and Cottages</div></div>
  <div class="type-tile"><div class="type-photo" role="img" aria-label="Sunset over the water" style="background:linear-gradient(180deg,#e3a45a,#2e3c55)"></div><div class="type-label">Waterfront Lots</div></div>
  <div class="type-tile"><div class="type-photo" role="img" aria-label="Country home and cottage" style="background:linear-gradient(180deg,#9cbad2,#7b5c45)"></div><div class="type-label">Homes and Cottages</div></div>
  <div class="type-tile"><div class="type-photo" role="img" aria-label="Farm acreage with barn" style="background:linear-gradient(180deg,#a9c2d6,#6f8b4a)"></div><div class="type-label">Lots, Acreages and Farms</div></div>
  <div class="type-tile"><div class="type-photo" role="img" aria-label="Commercial building on main street" style="background:linear-gradient(180deg,#8fb0cf,#6a6f74)"></div><div class="type-label">Commercial and Businesses</div></div>
  <div class="type-tile"><div class="type-photo" role="img" aria-label="Luxury waterfront residence" style="background:linear-gradient(180deg,#7fa8cf,#3e5a7a)"></div><div class="type-label">Luxury Properties</div></div>
</section>

<section class="content-panels">
  <article class="panel about">
    <h2>About <span>Me</span></h2>
    <div class="about-body">
      <div class="about-top">
        <div class="portrait" role="img" aria-label="Portrait of Lorena Paskett"></div>
        <p>Lorem ipsum dolor sit amet, consectetur adipisicing elit, sed do eiusmod tempor incididunt ut labore et dolore magna aliqua. Ut enim ad minim veniam.</p>
      </div>
      <p>Lorem ipsum dolor sit amet, consectetur adipisicing elit, sed do eiusmod tempor incididunt ut labore et dolore magna aliqua. Ut enim ad minim veniam, quis nostrud exercitation ullamco laboris.</p>
    </div>
    <a class="read-more" href="#">[Read More]</a>
  </article>

  <article class="panel featured">
    <h2>Featured <span>Properties</span></h2>
    <div class="featured-body">
      <div class="featured-photo" role="img" aria-label="Lakeside property with trees" style="background:linear-gradient(180deg,#8fb4d6,#3f6a3a)">
        <svg width="30" height="30" viewBox="0 0 30 30"><circle cx="15" cy="15" r="14" fill="rgba(0,0,0,.45)"/><circle cx="13" cy="13" r="5" fill="none" stroke="#fff" stroke-width="2"/><path d="M17 17l5 5" stroke="#fff" stroke-width="2.5"/></svg>
      </div>
      <div class="featured-photo" role="img" aria-label="Shoreline with boats and forest" style="background:linear-gradient(180deg,#5b8a4e,#4f7fae)">
        <svg width="30" height="30" viewBox="0 0 30 30"><circle cx="15" cy="15" r="14" fill="rgba(0,0,0,.45)"/><circle cx="13" cy="13" r="5" fill="none" stroke="#fff" stroke-width="2"/><path d="M17 17l5 5" stroke="#fff" stroke-width="2.5"/></svg>
      </div>
    </div>
    <a class="read-more" href="#">[View More]</a>
  </article>

  <article class="panel testimonials">
    <h2>Testimonials</h2>
    <div class="testimonial-body">
      <p>Lorem ipsum dolor sit amet, consectetur adipisicing elit, sed do eiusmod tempor incididunt ut labore et dolore magna aliqua. Ut enim ad minim veniam, quis nostrud exercitation.</p>
      <p>Lorem ipsum dolor sit amet, consectetur adipisicing elit, sed do eiusmod tempor incididunt ut labore et dolore magna aliqua. Ut enim ad minim veniam, quis nostrud.</p>
      <div class="writer">— Writer's Name</div>
    </div>
    <a class="read-more" href="#">[Read More]</a>
  </article>
</section>

<footer class="site-footer">
  <div class="footer-col quick-links">
    <h3>Quick Links</h3>
    <div class="lists">
      <ul><li>Home</li><li>Local Services</li><li>Weather</li><li>Water Levels</li></ul>
      <ul><li>Follow Me</li><li>Articles</li><li>Tips for PTR Search</li></ul>
    </div>
  </div>
  <div class="footer-col contact-col">
    <h3>Contact Me</h3>
    <ul>
      <li><span>Toll Free</span>: 1-888-555-0172</li>
      <li><span>Phone</span>: 519-555-0148</li>
      <li><span>Email</span>: lorena@hartwellnobe.com</li>
    </ul>
  </div>
  <div class="footer-col follow-col">
    <h3>Follow Me</h3>
    <div class="social-grid">
      <div class="social-dot" aria-label="Chatterly"></div>
      <div class="social-dot" aria-label="Peeplet"></div>
      <div class="social-dot alt" aria-label="PostMill"></div>
      <div class="social-dot" aria-label="Workloop"></div>
      <div class="social-dot warm" aria-label="Vidnook"></div>
      <div class="social-dot warm" aria-label="Clipwall"></div>
    </div>
  </div>
  <div class="footer-col badge-col">
    <div class="partner-badge"></div>
    <p class="badge-note">Top producing agent in the region, serving the Fenwick Headland for many years.</p>
  </div>
  <div class="copyright">Copyright © 2013, Lorena Paskett<br>All rights reserved.</div>
</footer>

</body>
</html>
```